Frostvale Cool Packs needs stationery designed for their new logo

We have a new logo so now want all our stationery to be redesigned.
Frostvale is a gel ice pack product used by the seafood & food industry to transport chilled products around the world.

We would like to use our new logo with icy or snow backgrounds or elements.
Our company tag line is "Keep your products chilled for longer"
I'll attach our old business cards so that you can use the text off them.
2nd attachment is our new logo to be used.

We want a design for:
- Business cards
- Letter Head
- Email signature

Target Market(s)

seafood & chilled food distributors

Industry/Entity Type

Industry

Font styles to use
Sans Serif

Colors
0492cd
85cae6
cee9f5

Requirements
Must have
• Our logo
Nice to have
• Snow or ice background or image incorporated somehow

```html
<!DOCTYPE html>
<html lang="en">
<head>
<meta charset="utf-8">
<title>Frostvale Cool Packs – Business Card Options</title>
<link href="https://fonts.googleapis.com/css2?family=Source+Sans+3:wght@400;600&family=Roboto+Condensed:wght@400&family=Tinos&display=swap" rel="stylesheet">
<style>
  :root {
    --sheet: #dcd5bd;
    --brand-blue: #0475bf;
    --ice-mid: #85cae6;
    --ice-light: #cee9f5;
    --ink: #222222;
    --logo-grey: #808285;
    --white: #ffffff;
  }
  * { box-sizing: border-box; margin: 0; padding: 0; }
  html, body { width: 1200px; height: 1200px; overflow: hidden; }
  body {
    background: var(--sheet);
    font-family: "Source Sans 3", Arial, sans-serif;
    position: relative;
  }
  .card {
    position: absolute;
    width: 358px;
    height: 221px;
    background: var(--white);
    overflow: hidden;
    box-shadow: 6px 7px 8px rgba(40, 35, 20, 0.55);
  }
  .card--blue { background: var(--brand-blue); color: var(--white); }
  .option-label {
    position: absolute;
    width: 200px;
    text-align: center;
    font-family: "Tinos", "Times New Roman", serif;
    font-size: 17px;
    color: #333;
  }
  .person { position: absolute; left: 26px; top: 18px; }
  .person__name { font-size: 14px; font-weight: 600; color: var(--brand-blue); line-height: 1.2; }
  .person__role { font-size: 9.5px; color: var(--ink); margin-top: 1px; }
  .card--blue .person__name, .card--blue .person__role { color: var(--white); }
  .contact { position: absolute; left: 26px; font-size: 8.6px; color: var(--ink); line-height: 12.5px; }
  .card--blue .contact { color: var(--white); font-size: 10px; line-height: 16px; }
  .contact__row { display: flex; align-items: center; gap: 6px; }
  .contact__row svg { width: 9px; height: 9px; flex: none; }
  .wordmark {
    position: absolute;
    font-weight: 600;
    color: var(--logo-grey);
    display: flex;
    align-items: center;
    gap: 6px;
    line-height: 1;
  }
  .wordmark__dot { border-radius: 50%; background: var(--brand-blue); flex: none; }
  .card--blue .wordmark { color: var(--white); }
  .card--blue .wordmark__dot { background: var(--white); }
  .tagline-band {
    position: absolute; left: 0; right: 0; bottom: 0; height: 25px;
    background: var(--brand-blue); color: var(--white);
    font-family: "Roboto Condensed", Arial, sans-serif;
    font-size: 14.5px; text-align: center; line-height: 25px;
  }
  .tagline {
    position: absolute;
    font-family: "Roboto Condensed", Arial, sans-serif;
    white-space: nowrap;
  }
  .frost-disc { position: absolute; border-radius: 50%; }
</style>
</head>
<body>

<!-- Front A -->
<section class="card" style="left:196px;top:69px;">
  <div class="person"><div class="person__name">Marcus Dale</div><div class="person__role">Business Development</div></div>
  <div class="wordmark" style="left:187px;top:28px;font-size:20px;"><span class="wordmark__dot" style="width:18px;height:18px;"></span>Frostvale</div>
  <div class="contact" style="top:155px;">
    <div class="contact__row"><svg viewBox="0 0 10 10"><rect x="0.5" y="2" width="9" height="6.5" fill="none" stroke="#0475bf" stroke-width="1.2"/><path d="M0.5 2 L5 6 L9.5 2" fill="none" stroke="#0475bf" stroke-width="1.2"/></svg>marcus.dale@frostvale.com.au</div>
    <div class="contact__row"><svg viewBox="0 0 10 10"><circle cx="5" cy="5" r="4.3" fill="none" stroke="#0475bf" stroke-width="1"/><ellipse cx="5" cy="5" rx="1.8" ry="4.3" fill="none" stroke="#0475bf" stroke-width="0.8"/><path d="M0.7 5 H9.3" stroke="#0475bf" stroke-width="0.8"/></svg>www.frostvale.com.au</div>
  </div>
  <div class="tagline-band">Keep your products chilled for longer</div>
</section>
<div class="option-label" style="left:200px;top:306px;">Front- A</div>

<!-- Front B -->
<section class="card" style="left:647px;top:70px;">
  <div class="person"><div class="person__name">Marcus Dale</div><div class="person__role">Business Development</div></div>
  <div class="wordmark" style="left:187px;top:28px;font-size:20px;"><span class="wordmark__dot" style="width:18px;height:18px;"></span>Frostvale</div>
  <div class="frost-disc" role="img" aria-label="Faint ice decoration" style="left:255px;top:105px;width:120px;height:120px;background:var(--ice-light);"></div>
  <div class="contact" style="top:155px;">
    <div class="contact__row"><svg viewBox="0 0 10 10"><rect x="0.5" y="2" width="9" height="6.5" fill="none" stroke="#0475bf" stroke-width="1.2"/><path d="M0.5 2 L5 6 L9.5 2" fill="none" stroke="#0475bf" stroke-width="1.2"/></svg>marcus.dale@frostvale.com.au</div>
    <div class="contact__row"><svg viewBox="0 0 10 10"><circle cx="5" cy="5" r="4.3" fill="none" stroke="#0475bf" stroke-width="1"/><ellipse cx="5" cy="5" rx="1.8" ry="4.3" fill="none" stroke="#0475bf" stroke-width="0.8"/><path d="M0.7 5 H9.3" stroke="#0475bf" stroke-width="0.8"/></svg>www.frostvale.com.au</div>
  </div>
  <div class="tagline-band">Keep your products chilled for longer</div>
</section>
<div class="option-label" style="left:704px;top:306px;">Front- B</div>

<!-- Front C -->
<section class="card" style="left:196px;top:348px;">
  <div class="person"><div class="person__name">Marcus Dale</div><div class="person__role">Business Development</div></div>
  <div class="frost-disc" role="img" aria-label="Large ice decoration" style="left:248px;top:112px;width:130px;height:130px;background:var(--brand-blue);"></div>
  <div class="contact" style="top:180px;">
    <div class="contact__row"><svg viewBox="0 0 10 10"><rect x="0.5" y="2" width="9" height="6.5" fill="none" stroke="#0475bf" stroke-width="1.2"/><path d="M0.5 2 L5 6 L9.5 2" fill="none" stroke="#0475bf" stroke-width="1.2"/></svg>marcus.dale@frostvale.com.au</div>
    <div class="contact__row"><svg viewBox="0 0 10 10"><circle cx="5" cy="5" r="4.3" fill="none" stroke="#0475bf" stroke-width="1"/><ellipse cx="5" cy="5" rx="1.8" ry="4.3" fill="none" stroke="#0475bf" stroke-width="0.8"/><path d="M0.7 5 H9.3" stroke="#0475bf" stroke-width="0.8"/></svg>www.frostvale.com.au</div>
  </div>
</section>
<div class="option-label" style="left:258px;top:581px;">Front- C</div>

<!-- Front D -->
<section class="card" style="left:647px;top:351px;">
  <div class="person" style="top:40px;"><div class="person__name">Marcus Dale</div><div class="person__role">Business Development</div></div>
  <div class="contact" style="left:163px;top:44px;">
    <div class="contact__row"><svg viewBox="0 0 10 10"><rect x="0.5" y="2" width="9" height="6.5" fill="none" stroke="#0475bf" stroke-width="1.2"/><path d="M0.5 2 L5 6 L9.5 2" fill="none" stroke="#0475bf" stroke-width="1.2"/></svg>marcus.dale@frostvale.com.au</div>
    <div class="contact__row"><svg viewBox="0 0 10 10"><circle cx="5" cy="5" r="4.3" fill="none" stroke="#0475bf" stroke-width="1"/><ellipse cx="5" cy="5" rx="1.8" ry="4.3" fill="none" stroke="#0475bf" stroke-width="0.8"/><path d="M0.7 5 H9.3" stroke="#0475bf" stroke-width="0.8"/></svg>www.frostvale.com.au</div>
  </div>
  <div class="wordmark" style="left:74px;top:127px;font-size:27px;"><span class="wordmark__dot" style="width:24px;height:24px;"></span>Frostvale</div>
  <div class="tagline" style="left:0;right:0;top:184px;text-align:center;font-family:'Source Sans 3',Arial,sans-serif;font-size:14.5px;color:var(--brand-blue);">Keep your products chilled for longer</div>
</section>
<div class="option-label" style="left:735px;top:581px;">Front- D</div>

<!-- Front E -->
<section class="card card--blue" style="left:199px;top:623px;">
  <div class="person"><div class="person__name">Marcus Dale</div><div class="person__role">Business Development</div></div>
  <div class="frost-disc" role="img" aria-label="Faint ice decoration" style="left:242px;top:106px;width:130px;height:130px;background:rgba(133,202,230,0.35);"></div>
  <div class="contact" style="top:170px;">
    <div class="contact__row"><svg viewBox="0 0 10 10"><rect x="0.5" y="2" width="9" height="6.5" fill="none" stroke="#fff" stroke-width="1.2"/><path d="M0.5 2 L5 6 L9.5 2" fill="none" stroke="#fff" stroke-width="1.2"/></svg>marcus.dale@frostvale.com.au</div>
    <div class="contact__row"><svg viewBox="0 0 10 10"><circle cx="5" cy="5" r="4.3" fill="none" stroke="#fff" stroke-width="1"/><ellipse cx="5" cy="5" rx="1.8" ry="4.3" fill="none" stroke="#fff" stroke-width="0.8"/><path d="M0.7 5 H9.3" stroke="#fff" stroke-width="0.8"/></svg>www.frostvale.com.au</div>
  </div>
</section>
<div class="option-label" style="left:278px;top:860px;">Front- E</div>

<!-- Back A -->
<section class="card card--blue" style="left:647px;top:629px;">
  <div class="frost-disc" role="img" aria-label="Faint ice decoration" style="left:240px;top:120px;width:130px;height:130px;background:rgba(133,202,230,0.35);"></div>
  <div class="wordmark" style="left:46px;top:78px;font-size:33px;"><span class="wordmark__dot" style="width:30px;height:30px;"></span>Frostvale</div>
  <div class="tagline" style="left:119px;top:122px;font-size:14.5px;color:var(--white);">Keep your products chilled for longer</div>
</section>
<div class="option-label" style="left:726px;top:860px;">Back- A</div>

<!-- Back B -->
<section class="card card--blue" style="left:199px;top:906px;">
  <div class="frost-disc" role="img" aria-label="Faint ice decoration" style="left:242px;top:106px;width:130px;height:130px;background:rgba(133,202,230,0.35);"></div>
  <div class="wordmark" style="left:54px;top:67px;font-size:33px;"><span class="wordmark__dot" style="width:30px;height:30px;"></span>Frostvale</div>
  <div class="tagline" style="left:52px;top:133px;font-size:18px;color:var(--white);">Keep your products chilled for longer</div>
</section>
<div class="option-label" style="left:280px;top:1141px;">Back- B</div>

<!-- Back C -->
<section class="card" style="left:647px;top:906px;">
  <div class="wordmark" style="left:46px;top:82px;font-size:33px;"><span class="wordmark__dot" style="width:30px;height:30px;"></span>Frostvale</div>
  <div class="tagline" style="left:119px;top:125px;font-size:14.5px;color:var(--brand-blue);">Keep your products chilled for longer</div>
</section>
<div class="option-label" style="left:732px;top:1141px;">Back- C</div>

</body>
</html>
```